Restaurant Menu for beach club in Martinique

We would like to set a new design for our Menu. We are a restaurant, and beach club, located in Martinique. Our website is available at : http://www.korenapalmeraie.com Regards

Low design quality

Colors

Designer to choose colors to be used in the design.

```html
<!DOCTYPE html>
<html lang="fr">
<head>
<meta charset="utf-8">
<title>Korena Palmeraie — Menu</title>
<link rel="stylesheet" href="https://fonts.googleapis.com/css2?family=Dancing+Script:wght@700&family=Great+Vibes&family=Open+Sans:wght@600&family=Quicksand:wght@500;600&display=swap">
<style>
  :root {
    --navy: #262d35;
    --gold: #c9a45a;
    --paper: #e8e8e6;
    --paper-light: #f1f1ef;
    --ink: #2b2f35;
    --bg: #d4d4d2;
  }
  * { box-sizing: border-box; margin: 0; padding: 0; }
  html, body { width: 1200px; height: 799px; overflow: hidden; }
  body { background: var(--bg); font-family: "Quicksand", sans-serif; color: var(--ink); }

  .sheet-row {
    position: absolute; left: 25px; top: 140px;
    display: flex; gap: 20px;
  }
  .page {
    position: relative; width: 370px; height: 520px;
    background: var(--navy); padding: 10px;
  }
  .page-inner {
    position: relative; width: 100%; height: 100%;
    border: 1.5px solid var(--gold);
    background: var(--paper); overflow: hidden;
  }

  .photo {
    position: absolute; left: 0; top: 0; width: 100%; height: 240px;
  }
  .photo--plats {
    background: linear-gradient(180deg, rgba(150,110,85,.9) 0%, rgba(200,185,170,.8) 55%, rgba(232,232,230,0) 100%),
                linear-gradient(90deg, #f4f1ec 0%, #b07a5a 60%, #7a5a45 100%);
  }
  .photo--entrees {
    background: linear-gradient(180deg, rgba(190,140,70,.85) 0%, rgba(170,120,100,.7) 50%, rgba(232,232,230,0) 100%),
                linear-gradient(90deg, #e0b060 0%, #6a2a2a 55%, #d8c9a8 100%);
  }

  .section-band {
    position: absolute; left: 0; top: 200px; width: 215px; height: 54px;
    background: var(--navy);
    display: flex; align-items: center; padding-left: 26px;
  }
  .section-band::before, .section-band::after {
    content: ""; position: absolute; left: 22px; width: 110px; height: 1px; background: var(--gold);
  }
  .section-band::before { top: 10px; }
  .section-band::after { bottom: 10px; }
  .section-title {
    font-family: "Open Sans", sans-serif; font-weight: 600;
    color: #f2f2f2; font-size: 21px; letter-spacing: 1px;
  }

  .dish-list { position: absolute; left: 30px; top: 262px; width: 300px; list-style: none; }
  .dish { position: relative; margin-bottom: 2px; }
  .dish-name {
    font-family: "Dancing Script", cursive; font-weight: 700;
    color: var(--gold); font-size: 14px; line-height: 14px; display: block;
  }
  .dish-desc { font-size: 7.5px; line-height: 9px; color: var(--ink); display: block; max-width: 195px; }
  .dish-price {
    position: absolute; right: 0; top: 2px;
    font-size: 8px; color: var(--gold); font-weight: 600;
  }

  .dish-photo {
    position: absolute; right: 14px; top: 410px; width: 100px; height: 44px;
    border-radius: 50%;
    background: radial-gradient(ellipse at center, #c9a58a 0%, #5f8a3a 45%, #c8553c 75%, #f2f2f2 100%);
  }

  .price-note {
    position: absolute; left: 50%; bottom: 14px; transform: translateX(-50%);
    border: 1px solid var(--ink); border-radius: 10px;
    padding: 2px 12px; font-size: 7px; white-space: nowrap; font-style: italic;
  }

  .cover .page-inner { background: var(--paper-light); border-color: transparent; }
  .page.cover { background: var(--paper-light); padding: 0; }
  .photo--cover {
    height: 290px;
    background: linear-gradient(180deg, rgba(160,200,225,.9) 0%, rgba(90,150,185,.85) 40%, rgba(200,170,180,.6) 65%, rgba(241,241,239,0) 100%),
                linear-gradient(90deg, #9cc6da 0%, #7eb2cc 50%, #e58c8c 75%, #c4a08a 100%);
  }
  .brand {
    position: absolute; top: 300px; left: 0; width: 100%;
    display: flex; align-items: center; justify-content: center; gap: 10px;
  }
  .brand-dot { width: 10px; height: 10px; border-radius: 50%; background: var(--ink); }
  .brand-name { font-weight: 600; font-size: 28px; color: var(--ink); letter-spacing: 1px; }
  .brand-rule {
    position: absolute; top: 352px; left: 40px; width: 290px; height: 1px; background: var(--ink);
  }
  .cover-title {
    position: absolute; top: 368px; left: 0; width: 100%; text-align: center;
    font-family: "Great Vibes", cursive; font-size: 46px; color: var(--ink);
  }
  .cover-lines { position: absolute; top: 425px; left: 40px; width: 290px; height: 20px; }
  .cover-url {
    position: absolute; bottom: 36px; left: 0; width: 100%; text-align: center;
    font-size: 14px; font-weight: 500; color: var(--ink); letter-spacing: .3px;
  }
</style>
</head>
<body>
<main class="sheet-row">

  <section class="page page--plats">
    <div class="page-inner">
      <div class="photo photo--plats" role="img" aria-label="Photo d'un plat de poisson grillé avec riz blanc et piment"></div>
      <div class="section-band"><h2 class="section-title">LES PLATS</h2></div>
      <ul class="dish-list">
        <li class="dish"><span class="dish-name">Le royal de foie gras</span><span class="dish-desc">et rouleau de printemps au poulet et vermicelles</span><span class="dish-price">10.50 €</span></li>
        <li class="dish"><span class="dish-name">Le tartare de St Jacques</span><span class="dish-desc">aux échalotes rôties et concombres</span><span class="dish-price">12.50 €</span></li>
        <li class="dish"><span class="dish-name">L'oeuf "cocotte"</span><span class="dish-desc">à la crème de morilles et jambon ibérique</span><span class="dish-price">9.50 €</span></li>
        <li class="dish"><span class="dish-name">La salade de légumes</span><span class="dish-desc">croquants et gambas façon thaï</span><span class="dish-price">9.80 €</span></li>
        <li class="dish"><span class="dish-name">Le foie gras de canard</span><span class="dish-desc">au vieux porto, brioche maison</span><span class="dish-price">13.80 €</span></li>
        <li class="dish"><span class="dish-name">Le gâteau de lapereau</span><span class="dish-desc">au lard paysan, farci au foie gras, compote<br>d'oignons rouges</span><span class="dish-price">9.80 €</span></li>
        <li class="dish"><span class="dish-name">La verrine aux 3 choux-fleurs,</span><span class="dish-desc">crabe et saumon fumé</span></li>
        <li class="dish"><span class="dish-name">Le foie gras frais</span></li>
      </ul>
      <div class="dish-photo" role="img" aria-label="Photo d'une assiette de salade composée"></div>
      <p class="price-note">Tous nos prix sont indiqués en TTC et comprennent la TVA à 5,5 %</p>
    </div>
  </section>

  <section class="page page--entrees">
    <div class="page-inner">
      <div class="photo photo--entrees" role="img" aria-label="Photo de rouleaux au sésame et betterave avec sauce"></div>
      <div class="section-band"><h2 class="section-title">LES ENTRÉES</h2></div>
      <ul class="dish-list">
        <li class="dish"><span class="dish-name">Le royal de foie gras</span><span class="dish-desc">et rouleau de printemps au poulet et vermicelles</span></li>
        <li class="dish"><span class="dish-name">Le tartare de St Jacques</span><span class="dish-desc">aux échalotes rôties et concombres</span></li>
        <li class="dish"><span class="dish-name">L'oeuf "cocotte"</span><span class="dish-desc">à la crème de morilles et jambon ibérique</span></li>
        <li class="dish"><span class="dish-name">La salade de légumes</span><span class="dish-desc">croquants et gambas façon thaï</span></li>
      </ul>
    </div>
  </section>

  <section class="page cover">
    <div class="page-inner">
      <div class="photo photo--cover" role="img" aria-label="Photo de cocktails sur une table face à la mer"></div>
      <div class="brand"><span class="brand-dot"></span><span class="brand-name">Korena Palmeraie</span></div>
      <div class="brand-rule"></div>
      <h1 class="cover-title">Menu</h1>
      <svg class="cover-lines" viewBox="0 0 290 20" aria-hidden="true">
        <g stroke="#2b2f35" stroke-width="1.2">
          <line x1="0" y1="14" x2="125" y2="10"/>
          <line x1="20" y1="18" x2="125" y2="14"/>
          <line x1="165" y1="10" x2="290" y2="6"/>
          <line x1="165" y1="14" x2="270" y2="10"/>
        </g>
        <circle cx="145" cy="12" r="1.6" fill="#2b2f35"/>
      </svg>
      <p class="cover-url">www.korenapalmeraie.com</p>
    </div>
  </section>

</main>
</body>
</html>
```